Dental Business Card

I need Dental oriented business cards.
On the front side -
- on the first line, my name:
Dr Marlo Vintner
- on the second line (just underneath):
Doctor of Dental Medicine
- on the third line, or underneath that or in a corner, I would like the address and phone number:
5182 Ch. Birchfield
Montreal QC H2T 4B9
514-629-5074
- other than that i would maybe like a logo of a tooth, but i want it to be subtle and very basic!
- I would like the card to be preferably black or dark grey-ish with the writing in white
On the other side -
- 2-3 lines with the possibility to write the next appointment the box with the lines should be white, with the rest of the card being black

```html
<!DOCTYPE html>
<html lang="en">
<head>
<meta charset="utf-8">
<title>Dr Marlo Vintner – Business Card</title>
<link rel="stylesheet" href="https://fonts.googleapis.com/css2?family=Poppins:wght@400;600&display=swap">
<style>
  :root {
    --backdrop: #b3b3b3;
    --card: #2f2c2d;
    --ink: #ffffff;
    --navy: #2e2a6b;
    --ice: #cfe6f2;
    --paper: #f6f6f6;
  }
  * { margin: 0; padding: 0; box-sizing: border-box; }
  html, body {
    width: 1200px;
    height: 1000px;
    overflow: hidden;
    background: var(--backdrop);
    font-family: "Poppins", sans-serif;
    color: var(--ink);
  }
  .card {
    position: absolute;
    background: var(--card);
    overflow: hidden;
  }
  .card--front { left: 335px; top: 175px; width: 528px; height: 302px; }
  .card--back  { left: 343px; top: 560px; width: 512px; height: 292px; }

  .identity { position: absolute; left: 48px; top: 58px; }
  .identity__name {
    font-size: 24px;
    font-weight: 600;
    line-height: 1.2;
    letter-spacing: 0.1px;
  }
  .identity__title {
    margin-top: 8px;
    font-size: 13.5px;
    font-weight: 400;
  }
  .divider {
    position: absolute;
    left: 48px;
    top: 147px;
    width: 24px;
    height: 2px;
    background: var(--ink);
  }
  .contact {
    position: absolute;
    left: 48px;
    top: 180px;
    font-size: 13.5px;
    line-height: 25px;
    list-style: none;
  }
  .contact__label { font-weight: 600; }
  .contact__indent { padding-left: 16px; }

  .tooth-mark {
    position: absolute;
    left: 326px;
    top: 33px;
    width: 240px;
    height: 300px;
    border-radius: 90px 40px 0 0;
    background: linear-gradient(160deg, var(--paper) 55%, var(--ice) 100%);
    box-shadow: inset 0 0 0 8px var(--navy);
  }

  .appointment__label {
    position: absolute;
    left: 46px;
    top: 70px;
    font-size: 15px;
    font-weight: 600;
  }
  .appointment__box {
    position: absolute;
    left: 46px;
    top: 106px;
    width: 421px;
    height: 140px;
    border-radius: 18px;
    background: var(--paper);
  }
</style>
</head>
<body>
  <section class="card card--front" aria-label="Business card front">
    <div class="identity">
      <h1 class="identity__name">Dr Marlo Vintner</h1>
      <p class="identity__title">Doctor of Dental Medicine</p>
    </div>
    <div class="divider"></div>
    <ul class="contact">
      <li><span class="contact__label">A:</span> 5182 Ch. Birchfield Montreal</li>
      <li class="contact__indent">QC H2T 4B9</li>
      <li><span class="contact__label">P:</span> 514-629-5074</li>
    </ul>
    <div class="tooth-mark" role="img" aria-label="Simple outlined tooth illustration"></div>
  </section>

  <section class="card card--back" aria-label="Business card back">
    <p class="appointment__label">Next Appoitment:</p>
    <div class="appointment__box"></div>
  </section>
</body>
</html>
```